Birchline Heating & Air

I need a business card made for my company. I would like my new logo for Birchline Heating and Air on the front and my Garage Door on the back.
Front to say -Heating & Air Conditioning , Mini Splits and Heat Pumps, Hydronic In-Floor Heat. Locally Owned and Operated! Licensed, Boned and Insured. Free Estimates on new equipment. 715-408-2159
BGD Back Card, change phone# to 651-374-5810. Remove Commercial and residential and fully sticked vans lines.

```html
<!DOCTYPE html>
<html lang="en">
<head>
<meta charset="utf-8">
<title>Birchline Heating &amp; Air – Business Card</title>
<link href="https://fonts.googleapis.com/css2?family=Archivo:wght@400;500;700;800&display=swap" rel="stylesheet">
<style>
  :root {
    --brand-red: #e0221a;
    --brand-blue: #0b4285;
    --paper: #f3f4f5;
    --rule: #7f9cc4;
    --backdrop: #d6d6d6;
    --white: #ffffff;
  }
  * { box-sizing: border-box; margin: 0; padding: 0; }
  html, body {
    width: 960px; height: 1200px; overflow: hidden;
    background: var(--backdrop);
    font-family: "Archivo", Arial, sans-serif;
  }
  .sheet {
    width: 960px; height: 1200px;
    display: flex; flex-direction: column; align-items: center; justify-content: center;
    gap: 70px;
  }
  .card {
    position: relative;
    width: 840px; height: 480px;
    background: var(--paper);
    overflow: hidden;
    box-shadow: 0 10px 30px rgba(0,0,0,.18);
  }
  .card-art { position: absolute; inset: 0; width: 100%; height: 100%; }

  .wordmark {
    position: absolute;
    display: flex; align-items: center; gap: 16px;
    color: var(--brand-blue);
    font-weight: 800;
    text-transform: uppercase;
    line-height: .95;
    letter-spacing: -.5px;
  }
  .wordmark-dot {
    flex: none; border-radius: 50%;
    background: var(--brand-red);
  }
  .card--contact .wordmark { left: 70px; top: 70px; font-size: 58px; }
  .card--contact .wordmark-dot { width: 56px; height: 56px; }
  .card--services .wordmark { left: 50px; top: 40px; font-size: 34px; }
  .card--services .wordmark-dot { width: 34px; height: 34px; }

  /* contact side */
  .contact-title {
    position: absolute; left: 250px; top: 262px;
    color: var(--white); font-size: 26px; font-weight: 500;
  }
  .contact-details {
    position: absolute; left: 250px; top: 350px;
    color: var(--white); font-size: 14px; line-height: 1.55;
  }
  .contact-divider {
    position: absolute; left: 505px; top: 352px;
    width: 1px; height: 42px; background: rgba(255,255,255,.7);
  }
  .contact-web {
    position: absolute; left: 530px; top: 350px;
    color: var(--white); font-size: 14px; line-height: 1.55;
  }
  .contact-web strong, .contact-details strong { font-weight: 700; }

  /* services side */
  .service-list {
    position: absolute; list-style: none;
    color: var(--brand-blue); font-size: 17px; font-weight: 500;
  }
  .service-list li { height: 32px; line-height: 32px; }
  .service-list li::before { content: "• "; }
  .service-list--left { left: 80px; top: 168px; }
  .service-list--right { left: 420px; top: 72px; }
  .offer {
    position: absolute; left: 40px; top: 348px;
    color: var(--white); font-size: 15px;
  }
  .offer strong { font-size: 30px; font-weight: 800; margin-right: 8px; }
</style>
</head>
<body>
<main class="sheet">

  <section class="card card--contact" aria-label="Business card, contact side">
    <svg class="card-art" viewBox="0 0 840 480" aria-hidden="true">
      <path fill="var(--brand-red)" d="M0 300 H200 C220 300 220 250 250 250 H560 C590 250 590 300 620 300 H840 V330 H0 Z"/>
      <rect x="0" y="330" width="840" height="80" fill="var(--brand-blue)"/>
      <path fill="var(--brand-red)" d="M200 300 H620 V340 C620 340 200 340 200 340 Z"/>
      <rect x="0" y="410" width="840" height="22" fill="var(--brand-red)"/>
      <rect x="0" y="440" width="840" height="8" fill="var(--brand-blue)"/>
      <rect x="0" y="456" width="840" height="24" fill="var(--brand-blue)"/>
    </svg>
    <div class="wordmark"><span class="wordmark-dot"></span><span>Birchline<br>Heating &amp; Air</span></div>
    <p class="contact-title">Contact Us</p>
    <p class="contact-details">Phone : <strong>651 - 374 - 5810</strong><br>Email : <strong>birchlinedoors@mail.com</strong></p>
    <span class="contact-divider"></span>
    <p class="contact-web">Visit our website<br><strong>www.birchlinegarage.com</strong></p>
  </section>

  <section class="card card--services" aria-label="Business card, services side">
    <svg class="card-art" viewBox="0 0 840 480" aria-hidden="true">
      <g stroke="var(--rule)" stroke-width="1">
        <line x1="0" y1="104" x2="840" y2="104"/>
        <line x1="0" y1="136" x2="840" y2="136"/>
        <line x1="0" y1="168" x2="840" y2="168"/>
        <line x1="0" y1="200" x2="840" y2="200"/>
        <line x1="0" y1="232" x2="840" y2="232"/>
        <line x1="0" y1="264" x2="840" y2="264"/>
      </g>
      <path fill="var(--brand-blue)" d="M520 330 C580 330 590 260 650 260 H840 V372 H560 C540 372 540 330 520 330 Z"/>
      <path fill="var(--brand-red)" d="M0 330 H480 C530 330 540 380 590 380 H840 V410 H0 Z"/>
      <rect x="0" y="420" width="840" height="8" fill="var(--brand-blue)"/>
      <rect x="0" y="438" width="840" height="42" fill="var(--brand-blue)"/>
    </svg>
    <div class="wordmark"><span class="wordmark-dot"></span><span>Birchline<br>Heating &amp; Air</span></div>
    <ul class="service-list service-list--left">
      <li>Heating &amp; Air Conditioning</li>
      <li>Hydronic In-Floor Heat</li>
    </ul>
    <ul class="service-list service-list--right">
      <li>Mini Splits and Heat Pumps</li>
      <li>Locally Owned and Operated! Licensed</li>
      <li>Boned and Insured</li>
    </ul>
    <p class="offer"><strong>Free</strong>Estimates on new equipment</p>
  </section>

</main>
</body>
</html>
```